Create a Graphic About YOURSELF and PixelHarbor

PixelHarbor would like you (designers) to create an awesome graphic to promote YOURSELF and your profile on PixelHarbor!

Your graphic should communicate your name, your services and should mention PixelHarbor.

The design should be perfect for sharing on Chatterly. Here's an example of what we'd like http://blog.pixelharbor-example.ca/article/333/pixelharbor-launches-3000-hire-me-social-design-contest

Once you submitted your design, we'd love you to share the design ('advertisement') and promote yourself and PixelHarbor to your friends and potential customers. So make your submissions great and get your friends to vote for your design by 'Liking' it on Chatterly!

Prizes:
$1500 - "PixelHarbor Community" prize awarded to the designer with the most Chatterly 'Likes'
5 x $50 for the next 5 'most liked' designs on Chatterly

$1000 - "Hire Me" prize awarded to the designer who receives the most client invites
5 x $50 for the next 5 'most invited' designers

In summary, this is a great opportunity for you to increase your exposure to PixelHarbor customers and win cash prizes. Show off your design skills and get hired by PixelHarbor customers from around the world!

Target Market(s)

Fans, friends and customers of YOU

Industry/Entity Type

Cash

Requirements
Must have
• 1) Include your PixelHarbor user name on the graphic so customers can find you in the PixelHarbor Designer Directory
2) Include the tagline "Hire Me on PixelHarbor.com!" in your graphic design.
3) Share your design's URL on our Chatterly wall at http://chatterly-example.com/pixelharbor and get your friends to 'like' your design.
Nice to have
• 1) Include a tagline that expresses your design approach/philosophy
2) Artwork dimensions: 403 x 403 px
3) You can submit more than 1 design!
Should not have
• You must own the copyright of any images you use including stock imagery.

```html
<!DOCTYPE html>
<html lang="en">
<head>
<meta charset="utf-8">
<title>Dorian Vale – Bright Visuals Studio</title>
<link rel="stylesheet" href="https://fonts.googleapis.com/css2?family=Great+Vibes&family=Cabin:wght@400&display=swap">
<style>
  :root {
    --ink: #000000;
    --cyan: #1ba6e2;
    --silver: #d9d9d9;
    --white: #ffffff;
    --portrait-light: #f6f6f6;
    --portrait-mid: #c4c4c4;
  }
  * { margin: 0; padding: 0; box-sizing: border-box; }
  html, body {
    width: 1200px;
    height: 1200px;
    overflow: hidden;
    background: var(--ink);
  }
  .promo {
    position: relative;
    width: 1200px;
    height: 1200px;
    background: var(--ink);
    overflow: hidden;
    font-family: "Cabin", "Gill Sans", sans-serif;
  }
  .studio-title {
    position: absolute;
    right: 50px;
    top: 140px;
    font-family: "Great Vibes", cursive;
    font-size: 114px;
    font-weight: 400;
    color: var(--cyan);
    white-space: nowrap;
    letter-spacing: 4px;
    line-height: 1;
  }
  .portrait {
    position: absolute;
    left: 0;
    top: 360px;
    width: 700px;
    height: 840px;
    background: radial-gradient(ellipse closest-side at 38% 60%,
      var(--portrait-light) 0%,
      var(--portrait-mid) 50%,
      rgba(0,0,0,0) 100%);
  }
  .identity {
    position: absolute;
    right: 40px;
    top: 768px;
    text-align: right;
  }
  .identity__name {
    font-size: 78px;
    font-weight: 400;
    color: var(--silver);
    line-height: 1;
    white-space: nowrap;
  }
  .identity__role {
    margin-top: 4px;
    margin-right: 10px;
    font-family: "Great Vibes", cursive;
    font-size: 70px;
    color: var(--cyan);
    line-height: 1;
    white-space: nowrap;
  }
  .hire-line {
    position: absolute;
    right: 92px;
    top: 1010px;
    font-size: 56px;
    color: var(--white);
    line-height: 1;
    white-space: nowrap;
  }
  .hire-arrow {
    position: absolute;
    left: 1106px;
    top: 1036px;
    width: 80px;
    height: 100px;
  }
  .site-mark {
    position: absolute;
    left: 440px;
    top: 1078px;
    display: flex;
    align-items: center;
    gap: 20px;
  }
  .site-mark__dot {
    width: 68px;
    height: 68px;
    border-radius: 50%;
    background: var(--cyan);
  }
  .site-mark__name {
    font-size: 78px;
    color: var(--white);
    line-height: 1;
    white-space: nowrap;
  }
</style>
</head>
<body>
  <main class="promo">
    <h1 class="studio-title">Bright Visuals Studio</h1>

    <div class="portrait" role="img" aria-label="High-contrast black and white portrait of the designer looking upward"></div>

    <div class="identity">
      <p class="identity__name">Dorian Vale</p>
      <p class="identity__role">Graphic Designer</p>
    </div>

    <p class="hire-line">Here me on</p>
    <svg class="hire-arrow" viewBox="0 0 80 100" aria-hidden="true">
      <path d="M14 8 C60 4 76 40 56 66 C46 78 32 82 20 80" fill="none" stroke="var(--cyan)" stroke-width="7" stroke-linecap="round"/>
      <path d="M8 80 L30 64 L28 94 Z" fill="var(--cyan)"/>
    </svg>

    <div class="site-mark">
      <span class="site-mark__dot"></span>
      <span class="site-mark__name">PixelHarbor.com</span>
    </div>
  </main>
</body>
</html>
```